Personal Chef Needs a Good Web Design

Hi everyone!
My name is Lev, I work as a private chef for last 10 years, traveling all around the world and cooking in private megayacht and villas.
I'm about to settle down in my hometown in Europe for a while. And therefore I need a website that will show my story, pics and recipes, nutritional advices and of course offer a Personal and Private Chef services( working for 4-5 families and bringing delicious food to their house).
My clients are extremely rich folks, but usually are down to earth ones.
I believe, the web site should be focused on attention to:
-VIP person's wife( as she is usually responsible for food for family) and be simple.
-to famous people agents and be on high level.

There will be about 10 different menus and 6 different service offers

--UPDATE--
Logo Design:
+My thoughts are- printed structure of the vegetable or fruit on a white font. Like you slice the buffalo tomato, put it in red paint and print it on the edge of the page. See attached files named logo. Can be any nice structured thing, like tomato, lemon, red cabbage etc.
+Classic logos with chef's hat or knives are good too.
+Need to have the space for me to add the name( the fonts can be provided)

Target Market(s)

Private person. 80% Russian clients.

Industry/Entity Type

Cooking

Coding

Coded - Design and coding required

Number of Pages Required

3 page

Requirements
Must have
• Contact form/ Request back call/ Schedule a free consultation
Nice to have
• The client will need to choose straight ahead from the range of services I offer, like:
• -Private Chef( cooking only for the client)
• -Personal Chef( cooking for around 5 clients, bringing the ready to be heated food to their door)
• -Romantic dinner for two
• -Professional Sommelier service
• -Build your kitchen( offering design, equipment and that will fit your requirements)
• -Other( flowers, waiters, barista, equipment rental)
• So this column should go right after the introduction/aboutme part and will lead to separate pages with how-it-works thing for each.

```html
<!DOCTYPE html>
<html lang="en">
<head>
<meta charset="utf-8">
<title>Chef Lev — Private &amp; Personal Chef</title>
<link rel="stylesheet" href="https://fonts.googleapis.com/css2?family=Raleway:wght@400;600;700;800&family=Open+Sans:wght@400;600&family=Playfair+Display:wght@700&display=swap">
<style>
:root{
  --red:#d8372c;
  --red-dark:#b92a21;
  --ink:#222;
  --text:#666;
  --muted:#999;
  --line:#e4e4e4;
  --white:#fff;
  --night:#1e222c;
  --wood:#3b2a20;
  --wood-dark:#241811;
  --footer:#161616;
}
*{box-sizing:border-box;margin:0;padding:0}
html,body{width:1200px;height:5373px;overflow:hidden}
body{font-family:"Open Sans",Arial,sans-serif;color:var(--text);background:var(--white);font-size:13px;line-height:1.6;position:relative}
.h-title{font-family:"Raleway",Arial,sans-serif;font-weight:800;text-transform:uppercase;letter-spacing:1px;color:var(--red);font-size:30px;text-align:center}
.lead{text-align:center;font-size:13px;color:var(--muted);max-width:760px;margin:8px auto 0}
.btn{display:inline-block;background:var(--red);color:var(--white);font-family:"Raleway",sans-serif;font-weight:700;font-size:11px;text-transform:uppercase;padding:8px 16px;letter-spacing:.5px}
.ph{display:block}
section{position:absolute;left:0;width:1200px;overflow:hidden}

/* top bar */
.topbar{top:0;height:30px;background:#111;color:#bbb;font-size:11px;display:flex;justify-content:space-between;align-items:center;padding:0 120px}
.topbar span{display:inline-flex;align-items:center;gap:6px}
/* nav */
.nav{top:30px;height:105px;background:var(--white)}
.nav ul{list-style:none;display:flex;gap:34px;position:absolute;top:40px;font-family:"Raleway",sans-serif;font-weight:700;font-size:12px;color:var(--ink);text-transform:uppercase}
.nav .left{left:120px}.nav .right{right:120px}
.nav li.active{color:var(--red);border-bottom:2px solid var(--red);padding-bottom:4px}
.logo{position:absolute;left:540px;top:-22px;width:120px;height:120px;border-radius:50%;background:var(--white);border:3px solid var(--ink);display:flex;align-items:center;justify-content:center;font-family:"Raleway",sans-serif;font-weight:800;font-size:30px;color:var(--ink);z-index:3}
/* hero */
.hero{top:135px;height:440px}
.hero .ph{position:absolute;inset:0;background:linear-gradient(110deg,#3e4a2e 0%,#6d5a3c 30%,#2b2420 55%,#7d6a58 80%,#3a2e26 100%)}
.hero .shade{position:absolute;inset:0;background:linear-gradient(180deg,rgba(0,0,0,.15),rgba(0,0,0,.45))}
.hero h1{position:absolute;top:172px;width:100%;text-align:center;color:var(--white);font-family:"Raleway",sans-serif;font-weight:700;font-size:26px;letter-spacing:1px;text-transform:uppercase}
.hero .btn{position:absolute;top:226px;left:50%;transform:translateX(-50%)}
/* about */
.about{top:575px;height:517px}
.about .ph{position:absolute;left:0;top:0;width:540px;height:517px;background:linear-gradient(160deg,#e9e6e1,#b9afa3 55%,#8c7f72)}
.about .copy{position:absolute;left:560px;top:90px;width:560px}
.about h2{font-family:"Raleway",sans-serif;font-weight:800;font-size:30px;color:var(--red);text-transform:uppercase;border-left:4px solid var(--red);padding-left:14px;margin-bottom:20px}
.about p{font-size:12.5px;margin-bottom:14px}
.btn-dark{background:var(--ink)}
.deco-ring{position:absolute;border:1px solid #eee;border-radius:50%}
/* services */
.services{top:1092px;height:483px;background:#fbfbfb}
.services .h-title{margin-top:70px}
.svc-row{position:absolute;top:205px;left:160px;width:880px;display:flex;justify-content:space-between}
.svc{width:190px;text-align:center}
.svc svg{width:44px;height:44px;margin:0 auto 12px;display:block}
.svc h3{font-family:"Raleway",sans-serif;font-weight:700;font-size:12px;color:var(--red);text-transform:uppercase;margin-bottom:8px}
.svc p{font-size:11px;color:var(--muted);line-height:1.5}
.slide-arrow{position:absolute;top:225px}
/* menus */
.menus{top:1575px;height:358px;background:linear-gradient(90deg,var(--wood-dark),var(--wood) 30%,#4a3528 60%,var(--wood-dark))}
.menus .h-title{color:var(--white);margin-top:42px}
.menus .lead{color:#ccc}
.cats{position:absolute;top:210px;left:295px;display:flex;gap:44px}
.cat{width:50px;text-align:center;color:var(--white);font-family:"Raleway",sans-serif;font-weight:700;font-size:9.5px;text-transform:uppercase}
.cat .dot{width:46px;height:46px;border-radius:50%;background:#1c1410;border:2px solid #5a4536;margin:0 auto 8px;display:flex;align-items:center;justify-content:center}
.cat.active .dot{background:var(--red);border-color:var(--red)}
.cat.active{color:var(--red)}
/* seafood */
.seafood{top:1933px;height:573px;background:linear-gradient(135deg,#0f0f10,#242322 50%,#131313)}
.seafood .h-title{margin-top:75px}
.dishes{position:absolute;top:178px;left:150px;width:900px;display:flex;gap:28px}
.dish{width:282px;height:270px;background:var(--white);text-align:center;padding:24px 20px}
.dish h3{font-family:"Playfair Display",serif;font-size:17px;color:var(--ink);line-height:1.3;height:46px}
.dish .plate{width:160px;height:95px;margin:14px auto;border-radius:50%;background:radial-gradient(circle,#c98a4a 0%,#e9d9c2 45%,#fafafa 70%,#eee 100%)}
.dish .order{display:inline-block;border:1px solid #bbb;font-size:11px;color:var(--ink);padding:6px 14px}
.sq-arrow{position:absolute;top:285px;width:44px;height:44px;background:var(--red);display:flex;align-items:center;justify-content:center}
/* recipes */
.recipes{top:2506px;height:841px}
.recipes .h-title{margin-top:70px}
.filters{position:absolute;top:250px;width:100%;display:flex;justify-content:center;gap:8px}
.filters span{font-size:10.5px;padding:4px 14px;border:1px solid var(--line);color:#777}
.filters span.on{background:var(--red);color:var(--white);border-color:var(--red)}
.grid{position:absolute;top:325px;left:0;width:1200px;display:grid;grid-template-columns:repeat(5,240px);grid-auto-rows:250px}
.tile{position:relative}
.tile .cap{position:absolute;left:16px;right:16px;top:58%;background:var(--white);color:var(--ink);font-family:"Raleway",sans-serif;font-weight:700;font-size:12px;text-align:center;padding:5px 6px;line-height:1.3}
/* consult */
.consult{top:3347px;height:483px;background:var(--night)}
.consult .ph{position:absolute;left:0;top:0;width:502px;height:483px;background:linear-gradient(135deg,#8a2a1b,#c9512e 35%,#6f7a32 65%,#3a2a1c)}
.consult h2{position:absolute;left:600px;top:60px;font-family:"Raleway",sans-serif;font-weight:800;font-size:24px;color:var(--red);text-transform:uppercase}
.form{position:absolute;left:612px;top:140px;width:460px;display:grid;grid-template-columns:1fr 1fr;gap:16px 20px}
.field{height:30px;border:1px solid #3a4050;background:#262b36;color:#aab;font-size:11px;padding:6px 10px}
.field.full{grid-column:1/3;height:100px}
.form .btn{grid-column:1/3;justify-self:center;padding:7px 28px}
/* advices */
.advices{top:3830px;height:537px}
.advices .h-title{margin-top:52px}
.cards{position:absolute;top:168px;left:168px;display:flex;gap:16px}
.card{width:278px;text-align:center}
.card .ph{height:150px}
.card h3{font-family:"Playfair Display",serif;font-size:16px;color:var(--ink);margin:12px 0 6px}
.card p{font-size:11px;color:var(--muted);padding:0 12px;margin-bottom:10px}
.card .btn{padding:4px 10px;font-size:10px}
.pager{position:absolute;left:0;width:100%;display:flex;justify-content:center;gap:6px}
.pager i{display:block;width:12px;height:4px;background:#ccc}
.pager i.on{background:var(--red);width:24px}
/* testimonials */
.testi{top:4367px;height:376px;background:linear-gradient(90deg,#2a1c14,#4a3324 50%,#2a1c14)}
.quote{position:absolute;top:62px;width:445px;height:150px;background:var(--white);padding:18px 22px;font-size:11.5px;color:#777}
.quote b{color:var(--red);font-weight:600;font-size:11px}
.avatar{position:absolute;top:228px;width:52px;height:52px;border-radius:50%;background:linear-gradient(135deg,#d8d0c6,#8f8478);border:3px solid var(--white)}
.who{position:absolute;top:244px;color:var(--white);font-size:11px}
.dots{position:absolute;top:320px;width:100%;display:flex;justify-content:center;gap:8px}
.dots i{width:10px;height:10px;border-radius:50%;border:1px solid #aaa;display:block}
.dots i.on{background:var(--white)}
/* newsletter */
.news{top:4743px;height:197px;background:#f7f7f7}
.news p{position:absolute;top:52px;width:100%;text-align:center;font-size:14px;color:var(--ink);font-weight:600}
.news .row{position:absolute;top:100px;left:400px;display:flex}
.news .in{width:300px;height:32px;border:1px solid #ddd;background:var(--white);font-size:11px;color:#aaa;padding:7px 12px}
.news .btn{height:32px;padding:9px 18px}
/* footer */
.footer{top:4940px;height:394px;background:var(--footer);color:#9a9a9a;font-size:11.5px}
.footer h4{font-family:"Raleway",sans-serif;font-weight:700;font-size:14px;color:var(--white);text-transform:uppercase;margin-bottom:16px;letter-spacing:.5px}
.f-about{position:absolute;left:150px;top:50px;width:260px}
.f-logo{width:70px;height:70px;border-radius:50%;border:2px solid #666;display:flex;align-items:center;justify-content:center;font-family:"Raleway",sans-serif;font-weight:800;font-size:18px;color:#ddd;margin-bottom:16px}
.f-about p{margin-bottom:10px;line-height:1.5}
.f-recipes{position:absolute;left:478px;top:50px;width:250px}
.f-item{display:flex;gap:12px;margin-bottom:16px}
.f-item .ph{width:60px;height:46px;flex:none}
.f-item span{font-size:10.5px;color:#ccc;text-transform:uppercase;line-height:1.4}
.f-feed{position:absolute;left:772px;top:50px;width:280px}
.f-feed .sub{color:#6aa8e0;font-size:12px;margin:-6px 0 10px}
.feed{display:grid;grid-template-columns:repeat(4,64px);gap:6px}
.feed .ph{height:54px}
.bottombar{top:5334px;height:39px;background:#0c0c0c;color:#777;font-size:10.5px;padding:12px 120px}
</style>
</head>
<body>

<section class="topbar">
  <span><svg width="10" height="12" viewBox="0 0 10 12"><path d="M5 0a4 4 0 0 0-4 4c0 3 4 8 4 8s4-5 4-8a4 4 0 0 0-4-4z" fill="#d8372c"/></svg>18 Harbour Lane, Old Town, Riga</span>
  <span><svg width="11" height="11" viewBox="0 0 12 12"><path d="M2 1l3 1-1 2 4 4 2-1 1 3-2 1C5 11 1 7 1 3z" fill="#d8372c"/></svg>(371) 555 0142 <svg width="12" height="9" viewBox="0 0 12 9"><rect x=".5" y=".5" width="11" height="8" fill="none" stroke="#d8372c"/><path d="M.5.5L6 5l5.5-4.5" fill="none" stroke="#d8372c"/></svg>hello@cheflev.eu</span>
</section>

<section class="nav" style="overflow:visible;z-index:4">
  <ul class="left"><li class="active">Home</li><li>About Lev</li><li>Services</li><li>Recipes</li></ul>
  <div class="logo">LEV</div>
  <ul class="right"><li>Gallery</li><li>Blog</li><li>Testimonial</li><li>Contact</li></ul>
</section>

<section class="hero">
  <div class="ph" role="img" aria-label="Chef plating dishes in a professional kitchen, fresh vegetables in the foreground"></div>
  <div class="shade"></div>
  <h1>Soul in food comes with cooking with love</h1>
  <span class="btn">Hire me as personal chef</span>
</section>

<section class="about">
  <div class="ph" role="img" aria-label="Portrait of Chef Lev in a white chef's jacket"></div>
  <div class="deco-ring" style="right:-60px;top:240px;width:260px;height:260px"></div>
  <div class="copy">
    <h2>About Chef Lev</h2>
    <p>My name is Lev and here is Chef. For ten years I cooked for private families on yachts and in villas around the world. Every season brought new markets, new produce and new people to feed, and each menu was built around the guests at the table. After years of travel I am settling in my hometown, where I bring the same care to a small circle of families who want fresh, honest food every day.</p>
    <p>Our first consultation will be in your home. We will discuss any food preferences you may have, as well as any allergy or dietary needs. At that time we will also discuss what kind of meals you like, favourite recipes and cuisines, and how often you would like me to cook. If you have concerns about your diet we can work with any restrictions you have.</p>
    <span class="btn btn-dark">More about me</span>
  </div>
</section>

<section class="services">
  <h2 class="h-title">Services</h2>
  <p class="lead">Choose the service that suits your home, from daily family meals to a single evening for two.</p>
  <svg class="slide-arrow" style="left:80px" width="14" height="24" viewBox="0 0 14 24"><path d="M12 2L2 12l10 10" fill="none" stroke="#555" stroke-width="2"/></svg>
  <svg class="slide-arrow" style="right:80px" width="14" height="24" viewBox="0 0 14 24"><path d="M2 2l10 10L2 22" fill="none" stroke="#555" stroke-width="2"/></svg>
  <div class="svc-row">
    <div class="svc"><svg viewBox="0 0 44 44"><path d="M12 22a8 8 0 0 1 4-15 9 9 0 0 1 12 0 8 8 0 0 1 4 15v10H12z" fill="none" stroke="#222" stroke-width="2"/><line x1="12" y1="27" x2="32" y2="27" stroke="#222" stroke-width="2"/></svg><h3>Private Chef</h3><p>Cooking only for you and your family, in your own kitchen, every day.</p></div>
    <div class="svc"><svg viewBox="0 0 44 44"><rect x="8" y="14" width="28" height="20" fill="none" stroke="#222" stroke-width="2"/><path d="M8 20h28M16 14V9h12v5" fill="none" stroke="#222" stroke-width="2"/></svg><h3>Personal Chef</h3><p>Fresh meals for a few families, delivered to your door ready to heat.</p></div>
    <div class="svc"><svg viewBox="0 0 44 44"><path d="M14 6h8l-1 12a3 3 0 0 1-6 0zM18 21v15M13 36h10M30 6v30M27 6v10h6V6" fill="none" stroke="#222" stroke-width="2"/></svg><h3>Romantic Dinner for Two</h3><p>A quiet evening with a tasting menu served at your own table.</p></div>
    <div class="svc"><svg viewBox="0 0 44 44"><rect x="8" y="8" width="28" height="28" fill="none" stroke="#222" stroke-width="2"/><circle cx="16" cy="16" r="3" fill="none" stroke="#222" stroke-width="2"/><circle cx="28" cy="16" r="3" fill="none" stroke="#222" stroke-width="2"/><path d="M8 24h28" stroke="#222" stroke-width="2"/></svg><h3>Build Your Kitchen</h3><p>Design and equipment planned to fit the way you cook at home.</p></div>
  </div>
</section>

<section class="menus">
  <h2 class="h-title">Our Menus</h2>
  <p class="lead">This menu is just a sample of what I love to offer. They all can be modified and adjusted to suit your budget, tastes and dietary needs.</p>
  <div class="cats">
    <div class="cat active"><div class="dot"><svg width="22" height="16" viewBox="0 0 22 16"><path d="M1 8c5-7 12-7 16 0-4 7-11 7-16 0zM17 8l4-5v10z" fill="#fff"/></svg></div>Seafood</div>
    <div class="cat"><div class="dot"><svg width="20" height="20" viewBox="0 0 20 20"><path d="M13 3a5 5 0 0 1 0 9l-6 6-3-3 6-6a5 5 0 0 1 3-6z" fill="#fff"/></svg></div>Chicken</div>
    <div class="cat"><div class="dot"><svg width="20" height="20" viewBox="0 0 20 20"><path d="M2 9h16a8 8 0 0 1-16 0z" fill="#fff"/></svg></div>Extra Salads</div>
    <div class="cat"><div class="dot"><svg width="20" height="20" viewBox="0 0 20 20"><ellipse cx="10" cy="10" rx="8" ry="6" fill="#fff"/></svg></div>Beef</div>
    <div class="cat"><div class="dot"><svg width="20" height="20" viewBox="0 0 20 20"><path d="M2 9h16a8 7 0 0 1-16 0z" fill="#fff"/><path d="M7 2v4M12 2v4" stroke="#fff" stroke-width="1.5"/></svg></div>Soups</div>
    <div class="cat"><div class="dot"><svg width="20" height="20" viewBox="0 0 20 20"><path d="M4 16C4 8 10 3 17 3c0 7-5 13-13 13z" fill="#fff"/></svg></div>Vegetarian</div>
    <div class="cat"><div class="dot"><svg width="20" height="20" viewBox="0 0 20 20"><rect x="3" y="5" width="14" height="10" rx="4" fill="#fff"/></svg></div>Pork</div>
  </div>
</section>

<section class="seafood">
  <h2 class="h-title">Seafood Dishes</h2>
  <div class="sq-arrow" style="left:0"><svg width="12" height="18" viewBox="0 0 12 18"><path d="M10 2L3 9l7 7" fill="none" stroke="#fff" stroke-width="2.5"/></svg></div>
  <div class="sq-arrow" style="right:0"><svg width="12" height="18" viewBox="0 0 12 18"><path d="M2 2l7 7-7 7" fill="none" stroke="#fff" stroke-width="2.5"/></svg></div>
  <div class="dishes">
    <div class="dish"><h3>Garlic and Herb Crusted Seabass</h3><div class="plate" role="img" aria-label="Plated seabass fillet with herbs"></div><span class="order">Order Now / View</span></div>
    <div class="dish"><h3>Penne in Vodka Sauce with Shrimp and Asparagus</h3><div class="plate" role="img" aria-label="Bowl of penne with shrimp and asparagus"></div><span class="order">Order Now / View</span></div>
    <div class="dish"><h3>Miso Salmon with a Ginger Jasmine Rice</h3><div class="plate" role="img" aria-label="Miso glazed salmon on jasmine rice"></div><span class="order">Order Now / View</span></div>
  </div>
</section>

<section class="recipes">
  <h2 class="h-title">Recipes Gallery</h2>
  <p class="lead">This menu is just a sample of what I love to offer. They all can be modified and adjusted to suit your budget, tastes and dietary needs.</p>
  <div class="filters"><span class="on">All</span><span>Seafood</span><span>Chicken</span><span>Extra Salads</span><span>Beef</span><span>Soups</span><span>Vegetarian</span><span>Pork</span></div>
  <div class="grid">
    <div class="tile ph" role="img" aria-label="Thai style pork with coconut couscous" style="background:linear-gradient(135deg,#7a5a2e,#c9a15a)"><div class="cap">Thai Style Pork with a Coconut Couscous</div></div>
    <div class="tile ph" role="img" aria-label="Curry spiced chicken breast" style="background:linear-gradient(135deg,#4e5a2a,#b08a3e)"><div class="cap">Curry Spiced Chicken Breast with a Yogurt Cilantro Sauce</div></div>
    <div class="tile ph" role="img" aria-label="Red pepper hummus salad" style="background:linear-gradient(135deg,#a7412a,#e2a35a)"><div class="cap">Red Pepper Hummus Salad with Feta</div></div>
    <div class="tile ph" role="img" aria-label="Miso salmon with jasmine rice" style="background:linear-gradient(135deg,#c26a3a,#e8c7a0)"><div class="cap">Miso Salmon with a Ginger Jasmine Rice</div></div>
    <div class="tile ph" role="img" aria-label="Beef tenderloin with mushroom brandy sauce" style="background:linear-gradient(135deg,#4a2618,#9b5b3a)"><div class="cap">Beef Tenderloin in a Mushroom Brandy Sauce</div></div>
    <div class="tile ph" role="img" aria-label="Chicken marsala with mushrooms" style="background:linear-gradient(135deg,#6b4220,#c4883f)"><div class="cap">Chicken Marsala Mushrooms</div></div>
    <div class="tile ph" role="img" aria-label="Slow roasted baby back ribs" style="background:linear-gradient(135deg,#5a1e12,#a8502a)"><div class="cap">Slow Roasted Baby Back Ribs with Bourbon BBQ Sauce</div></div>
    <div class="tile ph" role="img" aria-label="Maple dijon glazed pork medallions" style="background:linear-gradient(135deg,#704a2a,#c89a5e)"><div class="cap">Maple Dijon Glazed Pork Medallions</div></div>
    <div class="tile ph" role="img" aria-label="Chickpea burgers with homemade patties" style="background:linear-gradient(135deg,#7c6a34,#c7b070)"><div class="cap">Chickpea Burgers with a Homemade Patty</div></div>
    <div class="tile ph" role="img" aria-label="Beef stew with orange and rosemary" style="background:linear-gradient(135deg,#3e2514,#8c5a30)"><div class="cap">Beef Stew with Orange and Rosemary</div></div>
  </div>
</section>

<section class="consult">
  <div class="ph" role="img" aria-label="Fresh tomatoes, avocado, peppers and spices on a table"></div>
  <h2>Schedule a Free Consultation</h2>
  <div class="form">
    <div class="field">Name</div><div class="field">Phone</div>
    <div class="field">Email</div><div class="field">Number of People ▾</div>
    <div class="field full">Message</div>
    <span class="btn">Submit</span>
  </div>
</section>

<section class="advices">
  <h2 class="h-title">Nutritional Advices</h2>
  <p class="lead">Good nutrition is one of the keys to good health. You can improve your nutrition by regularly eating foods that have a lot of vitamins and minerals in them.</p>
  <div class="cards">
    <div class="card"><div class="ph" role="img" aria-label="Glasses of milk on a table" style="background:linear-gradient(135deg,#efe8dc,#c9b89a)"></div><h3>Don't Drink Sugar Calories</h3><p>Sugary drinks are the most fattening things you can put into your body.</p><span class="btn">Read More</span></div>
    <div class="card"><div class="ph" role="img" aria-label="Red cup of coffee" style="background:linear-gradient(135deg,#b3221c,#e9d6c6)"></div><h3>Don't Fear Coffee</h3><p>Coffee is healthy and rich in antioxidants when taken in moderation.</p><span class="btn">Read More</span></div>
    <div class="card"><div class="ph" role="img" aria-label="Grilled salmon with lemon" style="background:linear-gradient(135deg,#d9773e,#f1c9a0)"></div><h3>Eat Fatty Fish</h3><p>Pretty much everyone agrees that fish is healthy and good for you.</p><span class="btn">Read More</span></div>
  </div>
  <div class="pager" style="top:485px"><i class="on"></i><i></i><i></i></div>
</section>

<section class="testi">
  <div class="quote" style="left:150px">Lev cooked for our family all winter and every dinner felt like a small celebration. The children ate vegetables without a word, and guests always asked who our chef was. Reliable, discreet and truly talented in the kitchen. <br><b>Anna K.</b></div>
  <div class="quote" style="left:606px">We booked a romantic dinner for our anniversary and it was perfect from start to finish. The menu was planned around our tastes and the service was calm and warm. We will certainly invite him again. <br><b>Daniel R.</b></div>
  <div class="avatar ph" role="img" aria-label="Client photo" style="left:210px"></div><div class="who" style="left:272px">Anna K.</div>
  <div class="avatar ph" role="img" aria-label="Client photo" style="left:666px"></div><div class="who" style="left:728px">Daniel R.</div>
  <div class="dots"><i class="on"></i><i></i><i></i></div>
</section>

<section class="news">
  <p>Recive the last recipes directly in your mailbox</p>
  <div class="row"><div class="in">Your email</div><span class="btn">Subscribe</span></div>
</section>

<section class="footer">
  <div class="f-about">
    <div class="f-logo">LEV</div>
    <p>A private chef bringing seasonal, honest food to a small circle of families at home.</p>
    <p>18 Harbour Lane, Old Town, Riga<br>(371) 555 0142<br>hello@cheflev.eu</p>
  </div>
  <div class="f-recipes">
    <h4>Famous Recipes</h4>
    <div class="f-item"><div class="ph" role="img" aria-label="Glazed pork dish" style="background:linear-gradient(135deg,#6b3a1e,#c58a4a)"></div><span>Glazed pork medallions with a rosemary jus</span></div>
    <div class="f-item"><div class="ph" role="img" aria-label="Beef tenderloin dish" style="background:linear-gradient(135deg,#4a2214,#a05a34)"></div><span>Beef tenderloin in a mushroom brandy sauce</span></div>
    <div class="f-item"><div class="ph" role="img" aria-label="Chickpea burger" style="background:linear-gradient(135deg,#7a6230,#cfae6a)"></div><span>Chickpea burgers with a homemade patty</span></div>
  </div>
  <div class="f-feed">
    <h4>Photo Feed</h4>
    <div class="sub">Chef Lev</div>
    <div class="feed">
      <div class="ph" role="img" aria-label="Food photo" style="background:#8a4a2a"></div>
      <div class="ph" role="img" aria-label="Food photo" style="background:#c9a15a"></div>
      <div class="ph" role="img" aria-label="Food photo" style="background:#5a6a2e"></div>
      <div class="ph" role="img" aria-label="Food photo" style="background:#a8412a"></div>
      <div class="ph" role="img" aria-label="Food photo" style="background:#6b4a30"></div>
      <div class="ph" role="img" aria-label="Food photo" style="background:#d9a074"></div>
      <div class="ph" role="img" aria-label="Food photo" style="background:#3e2a1c"></div>
      <div class="ph" role="img" aria-label="Food photo" style="background:#b5743a"></div>
    </div>
  </div>
</section>

<section class="bottombar">© Copyright ChefLev 2016</section>

</body>
</html>
```